Click Buttons for our website

We need a Click button design for our website www.brevilo.dk:
- it should fit into our website's style and colors
- the buttons should be available in variable sizes (so they can accommodate from 1-7 word text)
- the buttons should be supplied as vector graphics (so we can resize them yourself)

The buttons are to replace the red text links we have on the site today, i.e. they are to be used to link to "contact us" page pdf's and such.

Brevilo is a Danish based IT Hosting and IT outsourcing Company selling business2business. our clients are medium sized companies with the need for It outsourcing.

```html
<!DOCTYPE html>
<html lang="en">
<head>
<meta charset="utf-8">
<title>Brevilo – Click Buttons</title>
<link rel="stylesheet" href="https://fonts.googleapis.com/css2?family=Arimo:wght@400&display=swap">
<style>
  :root {
    --canvas: #232323;
    --canvas-edge: #2c2c2c;
    --label: #ffffff;
    --red-core: #d90d0d;
    --red-mid: #b80808;
    --red-edge: #7e0202;
    --red-rim: #5a0000;
    --red-gloss-top: rgba(255,255,255,0.30);
    --red-gloss-bottom: rgba(255,255,255,0.10);
    --dark-face: #1d1d1d;
    --dark-rim: #3a3a3a;
    --dark-gloss-top: #4d4d4d;
    --dark-gloss-bottom: #2f2f2f;
    --shadow: rgba(0,0,0,0.55);
  }
  * { box-sizing: border-box; margin: 0; padding: 0; }
  html, body { width: 1122px; height: 1200px; overflow: hidden; }
  body {
    background: var(--canvas);
    box-shadow: inset 0 0 0 2px var(--canvas-edge);
    position: relative;
    font-family: "Arimo", Arial, sans-serif;
  }
  .button-set { position: absolute; inset: 0; }
  .btn {
    position: absolute;
    width: 345px;
    height: 75px;
    display: flex;
    align-items: center;
    justify-content: center;
    color: var(--label);
    font-size: 31px;
    letter-spacing: 0.5px;
    text-decoration: none;
    overflow: hidden;
  }
  .btn span { position: relative; z-index: 2; }
  .btn--red {
    left: 176px;
    background: radial-gradient(ellipse 70% 140% at 50% 60%, var(--red-core) 0%, var(--red-mid) 45%, var(--red-edge) 100%);
  }
  .btn--dark {
    left: 569px;
    background: var(--dark-face);
    border: 2px solid var(--dark-rim);
  }
  .btn.has-gloss::before {
    content: "";
    position: absolute;
    left: 0; right: 0; top: 0;
    height: 48%;
    z-index: 1;
  }
  .btn--red.has-gloss::before {
    background: linear-gradient(var(--red-gloss-top), var(--red-gloss-bottom));
  }
  .btn--dark.has-gloss::before {
    background: linear-gradient(var(--dark-gloss-top), var(--dark-gloss-bottom));
  }

  /* style 1: tab, rounded top, open bottom */
  .style-tab { top: 165px; border-radius: 10px 10px 0 0; }
  .style-tab.btn--red { box-shadow: inset 0 2px 0 rgba(255,255,255,0.15); }
  .style-tab.btn--dark { border-bottom: none; }

  /* style 2: pill, fully rounded */
  .style-rounded { top: 312px; border-radius: 13px; }
  .style-rounded.btn--red { border: 2px solid var(--red-rim); box-shadow: 0 2px 4px var(--shadow); }
  .style-rounded.btn--dark { box-shadow: 0 2px 4px var(--shadow); }

  /* style 3: square with drop shadow */
  .style-square { top: 465px; box-shadow: 0 5px 8px var(--shadow); }
  .style-square.btn--red { border: 1px solid var(--red-rim); }

  /* style 4: square, fading bottom */
  .style-fade { top: 610px; box-shadow: 0 6px 8px -4px var(--shadow); }
  .style-fade.btn--dark { border-bottom: none; }

  /* style 5: flat with shadow */
  .style-flat { top: 759px; box-shadow: 0 5px 8px var(--shadow); }

  /* style 6: flat tab, open bottom */
  .style-flat-tab { top: 919px; box-shadow: 0 4px 6px -3px var(--shadow); }
  .style-flat-tab.btn--dark { border-bottom: none; border-color: #303030; }
</style>
</head>
<body>
  <main class="button-set">
    <a class="btn btn--red has-gloss style-tab" href="#"><span>HOSTING</span></a>
    <a class="btn btn--dark has-gloss style-tab" href="#"><span>HOSTING</span></a>

    <a class="btn btn--red has-gloss style-rounded" href="#"><span>HOSTING</span></a>
    <a class="btn btn--dark has-gloss style-rounded" href="#"><span>HOSTING</span></a>

    <a class="btn btn--red has-gloss style-square" href="#"><span>HOSTING</span></a>
    <a class="btn btn--dark has-gloss style-square" href="#"><span>HOSTING</span></a>

    <a class="btn btn--red has-gloss style-fade" href="#"><span>HOSTING</span></a>
    <a class="btn btn--dark has-gloss style-fade" href="#"><span>HOSTING</span></a>

    <a class="btn btn--red style-flat" href="#"><span>HOSTING</span></a>
    <a class="btn btn--dark style-flat" href="#"><span>HOSTING</span></a>

    <a class="btn btn--red style-flat-tab" href="#"><span>HOSTING</span></a>
    <a class="btn btn--dark style-flat-tab" href="#"><span>HOSTING</span></a>
  </main>
</body>
</html>
```